Can you make a cool and versatile Tarnel Ventures Powerpoint template?
See www.tarnelventures.co.uk and http://www.linkedin.com/company/tarnel-ventures-ltd/ (on the right) to see how the logos are currently used - with interchangeably white and black backgrounds.
Target Market(s)
Marketing managers, product managers in HR technology, HR consultants
Industry/Entity Type
It Company
Font styles to use
Sans Serif
Requirements
Must have
- Master slide design, fonts, color theme, etc. Ideally two variations - one with white background (using colorful logo), one with a darker background (using black/white logo).

```html
<!DOCTYPE html>
<html lang="en">
<head>
<meta charset="utf-8">
<title>Tarnel Ventures – Presentation Template</title>
<link rel="stylesheet" href="https://fonts.googleapis.com/css2?family=PT+Sans:wght@400;700&display=swap">
<style>
:root{
  --page:#ffffff;
  --slide:#231f20;
  --ink:#ffffff;
  --muted:#d9d9d9;
  --lime:#cfdc2b;
  --lime-dark:#8c9a12;
  --orange:#f39200;
  --orange-deep:#e84e0f;
  --blue:#1ea7e1;
  --blue-deep:#0a4f9e;
  --magenta:#a3195b;
  --pink:#d1569a;
  --green:#7dc242;
  --row-a:#eddde4;
  --row-b:#f7eef2;
  --title-ink:#1d1d1b;
}
*{margin:0;padding:0;box-sizing:border-box}
html,body{width:1200px;height:738px;overflow:hidden;background:var(--page)}
body{position:relative;font-family:"PT Sans",Arial,sans-serif;color:var(--ink)}
.slide{position:absolute;width:379px;height:284px;background:var(--slide);overflow:hidden;box-shadow:2px 3px 4px rgba(0,0,0,.35)}
.s1{left:15px;top:74px}.s2{left:408px;top:74px}.s3{left:802px;top:74px}
.s4{left:15px;top:395px}.s5{left:408px;top:395px}

.brand{position:absolute;display:flex;align-items:center;gap:5px;font-size:12px;color:var(--ink)}
.brand .dot{width:9px;height:9px;border-radius:50%;background:var(--ink)}
.brand-top{left:13px;top:30px}
.brand-foot{right:8px;bottom:14px;font-size:9px}
.brand-foot .dot{width:7px;height:7px}

.strip{position:absolute;height:37px}
.strip.blue{left:0;top:60px;width:312px;background:linear-gradient(90deg,var(--blue-deep),var(--blue) 45%,#6fc6ef)}
.strip.orange{left:75px;top:103px;width:304px;background:linear-gradient(90deg,#7a1e08,var(--orange-deep) 35%,var(--orange) 70%,#f8b419)}
.strip.lime{left:0;top:145px;width:301px;background:linear-gradient(90deg,#4b5208,var(--lime-dark) 40%,var(--lime))}
.strip.pink{left:86px;top:187px;width:293px;background:linear-gradient(90deg,var(--magenta),var(--pink) 50%,#eab2d0)}

.cover-title{position:absolute;left:12px;top:232px;font-size:17px}
.cover-sub{position:absolute;left:12px;top:256px;font-size:11px;color:var(--blue)}

.header-photo{position:absolute;left:0;top:4px;width:102px;height:42px;background:linear-gradient(120deg,#5c6410,var(--lime-dark) 50%,var(--lime))}
.header-bar{position:absolute;left:106px;right:0;top:4px;height:42px;background:var(--lime);color:var(--title-ink);display:flex;align-items:center;justify-content:flex-end;padding-right:8px;font-size:16px}

.bullets{position:absolute;list-style:none;font-size:10.5px;line-height:1.25}
.bullets li{position:relative;padding-left:15px;margin-bottom:6px}
.bullets li::before{content:"•";position:absolute;left:3px;color:var(--blue)}
.bullets li.sub{padding-left:30px}
.bullets li.sub::before{content:"–";left:18px;color:var(--muted)}
.s2 .bullets{left:9px;top:52px;right:8px}
.s3 .bullets{left:9px;top:54px;width:150px;font-size:8.4px}
.s3 .bullets li{margin-bottom:7px}

.footer{position:absolute;left:0;right:0;bottom:0;height:9px;background:var(--orange);font-size:5px;display:flex;align-items:center;justify-content:space-between;padding:0 6px}

.chart{position:absolute;left:178px;top:58px;width:193px;height:178px;border:1px dashed #bdbdbd}
.chart-title{position:absolute;top:8px;width:100%;text-align:center;font-size:10px}
.chart svg{position:absolute;left:0;top:0}

.table-title{position:absolute;top:52px;width:100%;text-align:center;color:var(--pink);font-size:11px}
.table-lead{position:absolute;left:9px;top:72px;right:20px;font-size:9px;line-height:1.3}
.data{position:absolute;left:53px;top:117px;width:279px;border-collapse:collapse;font-size:8px;text-align:center;color:#333}
.data th{background:var(--magenta);color:var(--ink);font-weight:400;height:16px;border:1px solid #c99ab0}
.data td{height:15.5px;border:1px solid #fff;background:var(--row-a)}
.data tr:nth-child(even) td{background:var(--row-b)}
</style>
</head>
<body>

<section class="slide s1">
  <div class="brand brand-top"><span class="dot"></span>Tarnel Ventures</div>
  <div class="strip blue" role="img" aria-label="Blue-toned photo of dandelion seeds"></div>
  <div class="strip orange" role="img" aria-label="Orange-toned photo of dandelion seeds"></div>
  <div class="strip lime" role="img" aria-label="Lime-toned photo of dandelion seeds"></div>
  <div class="strip pink" role="img" aria-label="Pink-toned photo of dandelion seeds"></div>
  <h1 class="cover-title" style="font-weight:400">Presentation Title</h1>
  <p class="cover-sub">Mauris ac justo a magna hendrerit</p>
</section>

<section class="slide s2">
  <div class="header-photo" role="img" aria-label="Lime-toned photo of dandelion seeds"></div>
  <h2 class="header-bar" style="font-weight:400">Lorem ipsum dolor sit amet elit</h2>
  <ul class="bullets">
    <li>Aenean nec mollis velit. Vestibulum ante ipsum primis in faucibus orci luctus et ultrices posuere cubilia Curae.</li>
    <li>Maecenas facilisis magna sed arcu vehicula vestibulum. Donec non urna lectus.</li>
    <li>Etiam luctus feugiat diam non interdum. Aliquam dictum felis nec iaculis consectetur.</li>
    <li class="sub">Quisque eros dui, lobortis ut egestas at, aliquam vitae neque. Etiam nec luctus ante, tincidunt pharetra lacus.</li>
    <li class="sub">Aliquam eu arcu et enim viverra pretium. Mauris eu ligula pellentesque enim tristique malesuada fringilla a tortor. Nullam vel cursus metus.</li>
    <li>Phasellus vel urna vitae quam sollicitudin lacinia. Integer dolor lorem, feugiat in ligula in, vulputate dictum nisi.</li>
  </ul>
  <div class="brand brand-foot"><span class="dot"></span>Tarnel Ventures</div>
  <footer class="footer"><span>13-11-2013</span><span>Confidential</span><span>2</span></footer>
</section>

<section class="slide s3">
  <div class="header-photo" role="img" aria-label="Lime-toned photo of dandelion seeds"></div>
  <h2 class="header-bar" style="font-weight:400">Nullam vel cursus metus</h2>
  <ul class="bullets">
    <li>Phasellus vel urna vitae quam sollicitudin lacinia. Integer dolor lorem, feugiat in ligula in, vulputate dictum nisi.</li>
    <li>Proin rhoncus massa dui, non sodales libero auctor et.</li>
    <li>Duis volutpat pharetra ornare. Cras purus arcu, imperdiet et nunc et, semper ultrices turpis.</li>
    <li>Sed varius feugiat orci. Nulla sed ante a tortor viverra interdum id sed metus.</li>
  </ul>
  <figure class="chart">
    <figcaption class="chart-title">Graphic Title</figcaption>
    <svg width="193" height="178" viewBox="0 0 193 178">
      <g transform="rotate(-90 90 98)" fill="none" stroke-width="27">
        <circle cx="90" cy="98" r="46.5" stroke="var(--orange-deep)" stroke-dasharray="171.1 292.2"/>
        <circle cx="90" cy="98" r="46.5" stroke="var(--green)" stroke-dasharray="66.8 292.2" stroke-dashoffset="-171.1"/>
        <circle cx="90" cy="98" r="46.5" stroke="var(--magenta)" stroke-dasharray="29.2 292.2" stroke-dashoffset="-237.9"/>
        <circle cx="90" cy="98" r="46.5" stroke="var(--blue)" stroke-dasharray="25.1 292.2" stroke-dashoffset="-267.1"/>
      </g>
      <g fill="#fff" font-size="9" text-anchor="middle" font-family="PT Sans, Arial, sans-serif">
        <text x="132" y="113">8,2</text>
        <text x="53" y="115">3,2</text>
        <text x="54" y="72">1,4</text>
        <text x="77" y="56">1,2</text>
      </g>
    </svg>
  </figure>
  <div class="brand brand-foot"><span class="dot"></span>Tarnel Ventures</div>
  <footer class="footer"><span>13-11-2013</span><span>Confidential</span><span>3</span></footer>
</section>

<section class="slide s4">
  <div class="header-photo" role="img" aria-label="Lime-toned photo of dandelion seeds"></div>
  <h2 class="header-bar" style="font-weight:400">Nullam vel cursus metus</h2>
  <p class="table-title">Table title</p>
  <p class="table-lead">Quisque eros dui, lobortis ut egestas at, aliquam vitae neque. Etiam nec luctus ante, tincidunt pharetra lacus.</p>
  <table class="data">
    <thead><tr><th>Category A</th><th>Category B</th><th>Category C</th><th>Category D</th><th>Category E</th></tr></thead>
    <tbody>
      <tr><td>111.222</td><td>222.333</td><td>333.444</td><td>444.555</td><td>555.666</td></tr>
      <tr><td>222.333</td><td>111.222</td><td>444.555</td><td>999.111</td><td>777.888</td></tr>
      <tr><td>333.444</td><td>777.888</td><td>222.333</td><td>111.222</td><td>444.555</td></tr>
      <tr><td>444.555</td><td>888.666</td><td>555.666</td><td>222.333</td><td>999.111</td></tr>
      <tr><td>555.666</td><td>999.111</td><td>888.666</td><td>777.888</td><td>111.222</td></tr>
    </tbody>
  </table>
  <div class="brand brand-foot"><span class="dot"></span>Tarnel Ventures</div>
  <footer class="footer"><span>13-11-2013</span><span>Confidential</span><span>4</span></footer>
</section>

<section class="slide s5">
  <div class="brand brand-top"><span class="dot"></span>Tarnel Ventures</div>
  <div class="strip blue" role="img" aria-label="Blue-toned photo of dandelion seeds"></div>
  <div class="strip orange" role="img" aria-label="Orange-toned photo of dandelion seeds"></div>
  <div class="strip lime" role="img" aria-label="Lime-toned photo of dandelion seeds"></div>
  <div class="strip pink" role="img" aria-label="Pink-toned photo of dandelion seeds"></div>
  <h1 class="cover-title" style="font-weight:400">THANK YOU</h1>
  <p class="cover-sub">FOR YOUR TIME</p>
</section>

</body>
</html>
```